Clarinet Past Midnight: mini recital & soiree

I need a poster design for a recital I'm doing next Friday April 25. It's an "after party" from 10 - 1am where I'll be playing a 30 min program followed by a DJ and there'll be food wine etc. I want to see a very "sexy" kind of poster. Modern with a "south beach" kind of art deco feel but without the really cheesy connotation that south beach sometimes has (if that makes any sense). I've included the link for the Gatherlink event so you can get an idea of the feel I want.

Cheers!

https://www.gatherlink.example/events/519304762811095/

Target Market(s)

College Students at the Coral Ridge Institute

South Beach-ians

Industry/Entity Type

Events

Colors

Designer to choose colors to be used in the design.

Requirements
Must have
• Title of event..
Date..
Location..
Food / Beverage served..
DJ Torvik..

```html
<!DOCTYPE html>
<html lang="en">
<head>
<meta charset="utf-8">
<title>Clarinet Past Midnight – mini recital &amp; soirée</title>
<link rel="stylesheet" href="https://fonts.googleapis.com/css2?family=Archivo+Black&family=Open+Sans:wght@600&display=swap">
<style>
  :root {
    --page-bg: #e9e9e7;
    --ink-black: #050303;
    --deep-red: #6e0a04;
    --wine-red: #8a1a08;
    --warm-gold: #d99a1c;
    --soft-yellow: #f2d23a;
    --text-white: #ffffff;
  }
  html, body {
    margin: 0;
    padding: 0;
    width: 1200px;
    height: 1000px;
    overflow: hidden;
    background: var(--page-bg);
  }
  .canvas {
    position: relative;
    width: 1200px;
    height: 1000px;
  }
  .poster {
    position: absolute;
    left: 277px;
    top: 68px;
    width: 646px;
    height: 864px;
    overflow: hidden;
    background: var(--ink-black);
    color: var(--text-white);
    font-family: "Open Sans", Arial, sans-serif;
  }
  .poster__artwork {
    position: absolute;
    inset: 0;
    background:
      radial-gradient(ellipse 240px 300px at 520px 470px, rgba(217, 154, 28, 0.75) 0%, rgba(217, 154, 28, 0) 100%),
      radial-gradient(ellipse 300px 260px at 200px 140px, rgba(242, 210, 58, 0.35) 0%, rgba(242, 210, 58, 0) 100%),
      linear-gradient(90deg, rgba(110, 10, 4, 0) 80%, var(--deep-red) 100%),
      radial-gradient(ellipse 340px 360px at 320px 520px, var(--wine-red) 0%, var(--deep-red) 55%, rgba(110, 10, 4, 0) 100%),
      var(--ink-black);
  }
  .event-title {
    position: absolute;
    left: 166px;
    top: 172px;
    margin: 0;
    font-family: "Archivo Black", "Arial Black", sans-serif;
    font-weight: 400;
    font-size: 60px;
    line-height: 60px;
    letter-spacing: 0;
    text-shadow: 3px 3px 4px rgba(0, 0, 0, 0.75);
  }
  .event-title span { display: block; }
  .event-subtitle {
    position: absolute;
    left: 53px;
    top: 380px;
    margin: 0;
    font-size: 34px;
    line-height: 1;
    font-weight: 600;
  }
  .detail-heading,
  .detail-note {
    position: absolute;
    left: 53px;
    margin: 0;
    line-height: 1;
    font-weight: 600;
  }
  .detail-heading { font-size: 22px; }
  .detail-note { font-size: 11px; }
</style>
</head>
<body>
<div class="canvas">
  <article class="poster">
    <div class="poster__artwork" role="img" aria-label="Illustration of a glowing light trail swirling through deep red darkness around a brass saxophone"></div>

    <h1 class="event-title">
      <span>Clarinet</span>
      <span>Past</span>
      <span>Midnight</span>
    </h1>
    <p class="event-subtitle">mini recital &amp; soirée</p>

    <p class="detail-heading" style="top:581px">DJ Torvik</p>
    <p class="detail-note" style="top:611px">will be spinning for the night</p>

    <p class="detail-heading" style="top:645px">Food / Wine / Drink</p>
    <p class="detail-note" style="top:675px">will be served!!</p>

    <p class="detail-heading" style="top:707px">Friday April 25.</p>
    <p class="detail-note" style="top:744px">It's an "after party" from 10 - 1am</p>

    <p class="detail-heading" style="top:772px">Halvorsen Alumni Centre - Coral Ridge Institute</p>
    <p class="detail-note" style="top:810px">4180 Marisol Avenue, 33152 Palm Haven</p>
  </article>
</div>
</body>
</html>
```